Re jig a A4 Instructional Flyer

We need an established A4 instructional Flyer (2 pages x A4) - to be rejigged in Harcourt College of Learning Branding to look fresh and new.

Permissions have been received to rejig this Medical Triage Chart. Fresh branding and setting out (fonts) required.

FOOTER NOTES : to be inserted at the bottom of the A4 instruction sheet

Harcourt College produced with permissions from Outback Care Alliance, produced by Outback Care Alliance with Clinic Circle Uptown with permissions from Southern Lakes Carewell Hub. Harcourt acknowledges the NBFPS Standards Criterion 3.2.3 Practice Training and Education in Triage

Target Market(s)

Medical Practices

Industry/Entity Type

Health

Font styles to use
Serif

Colors
0255a3
f78f20

Requirements
Must have
• Professional
• Pops of colour in the chart.
• This chart is to be USED and is VISUAL (no boring grey words throughout)
• PROBS SANS SERIF but SERIF for titles OK
Nice to have
• look at www.harcourtlearn.edu.au FOR BRANDING look and feel

```html
<!DOCTYPE html>
<html lang="en">
<head>
<meta charset="utf-8">
<title>Front Desk Triage – Harcourt College of Learning</title>
<link href="https://fonts.googleapis.com/css2?family=Raleway:ital,wght@0,400;0,500;0,700;0,800;1,400;1,700&display=swap" rel="stylesheet">
<style>
  :root{
    --navy:#34496a;
    --orange:#d58f3f;
    --ink:#1d1d1d;
    --alert:#c42a2d;
    --alert-bg:#f5e4dd;
    --cat1:#8d5ba6;
    --cat2:#3b82c4;
    --cat3:#47a07c;
    --cat4:#e7b22c;
    --cat5:#ee7b22;
    --cat6:#e0457b;
  }
  *{box-sizing:border-box;margin:0;padding:0}
  html,body{width:1200px;height:848px;overflow:hidden;background:#fff}
  body{font-family:'Raleway',sans-serif;color:var(--ink);font-size:12px;line-height:1.22;position:relative}
  .abs{position:absolute}

  .brand{left:0;top:0;width:220px;height:148px;background:#fff;display:flex;flex-direction:column;align-items:center;justify-content:center;gap:8px}
  .brand-mark{width:14px;height:14px;background:var(--navy)}
  .brand-name{font-weight:700;color:var(--navy);font-size:12px;letter-spacing:.06em;text-align:center;line-height:1.3;text-transform:uppercase}
  .brand-tag{font-size:6.5px;color:var(--navy);letter-spacing:.05em;text-transform:uppercase}

  .masthead{left:220px;top:0;width:980px;height:134px;background:var(--navy);color:#fff;padding:24px 0 0 46px}
  .masthead h1{font-weight:500;font-size:30px;line-height:1.2}
  .masthead h1 strong{font-weight:800;font-size:43px;letter-spacing:.01em}
  .accent-band{left:220px;top:134px;width:980px;height:14px;background:var(--orange)}

  .hero-photo{left:380px;top:148px;width:820px;height:642px;
    background:radial-gradient(ellipse at 30% 40%,#c9d6de 0%,rgba(230,236,240,0) 45%),
               linear-gradient(90deg,#fff 0%,#eef2f4 30%,#f2ebe6 70%,#e6dcd5 100%)}

  h2{font-weight:800;font-size:13px;text-transform:uppercase;margin-bottom:10px}
  p,li{margin-bottom:8px}
  ul{list-style:none}
  ul.dots li{padding-left:10px;text-indent:-8px}
  ul.dots li::before{content:"·";margin-right:4px}
  em{font-style:italic}

  .col-left{left:52px;top:190px;width:300px}
  .steps{list-style:none}
  .steps li{margin-bottom:7px}
  .steps b{font-weight:700;margin-right:3px}

  .action-plan{left:37px;top:620px;width:344px;height:137px;background:var(--alert-bg);border:1.5px solid var(--alert);padding:14px 12px}
  .action-plan h3{color:var(--alert);font-weight:800;font-size:12px;margin-bottom:7px}
  .action-plan li{margin-bottom:1px}
  .action-plan .call{color:var(--alert);font-weight:800;margin-top:13px;font-size:12px}

  .panel{background:rgba(255,255,255,.82);padding:14px 14px}
  .panel-clinic{left:395px;top:180px;width:350px;height:348px;padding-top:10px}
  .cat{margin-bottom:13px}
  .cat span{font-weight:800}
  .c1{color:var(--cat1)}.c2{color:var(--cat2)}.c3{color:var(--cat3)}.c4{color:var(--cat4)}.c5{color:var(--cat5)}.c6{color:var(--cat6)}
  .panel-disease{left:395px;top:540px;width:350px;height:217px}
  .panel-disease h2{line-height:1.25}
  .panel-disease h2 .justified{display:block;text-align:justify;text-align-last:justify}
  .panel-schedule{left:763px;top:180px;width:315px;height:455px;padding-top:10px}
  .panel-schedule li{margin-bottom:10px}

  .record-note{left:763px;top:658px;width:315px;height:94px;background:rgba(214,220,236,.9);padding:12px 14px;font-weight:700;font-style:italic;text-align:justify;line-height:1.18}

  .footer{left:0;top:790px;width:1200px;height:58px;background:var(--navy);color:#fff;font-size:9.5px;display:flex;justify-content:space-between;align-items:center;padding:0 22px 0 28px}
  .footer .credits{font-style:italic;width:625px;font-size:8.8px;color:#dde3ec}
</style>
</head>
<body>

<div class="abs brand">
  <div class="brand-mark"></div>
  <div class="brand-name">Harcourt College<br>of Learning</div>
  <div class="brand-tag">Building Skills | Shaping Futures</div>
</div>

<header class="abs masthead">
  <h1><strong>FRONT DESK TRIAGE:</strong> How to manage common<br>scenarios faced by reception staff</h1>
</header>
<div class="abs accent-band"></div>

<div class="abs hero-photo" role="img" aria-label="Soft-focus photo of a smiling doctor with a stethoscope, colleague blurred in the background"></div>

<section class="abs col-left">
  <h2>Is this an emergency?</h2>
  <ul class="dots">
    <li>When answering the telephone, all callers should be asked if the matter is an emergency prior to being placed on hold: Ask the patient, <em>“Is this an emergency or can I place you on hold for a moment?”</em></li>
    <li>Consider the <b>TRIAGE STEPS</b> and <b>CATEGORIES</b> listed on the reverse of this document to assess the patient’s status.</li>
  </ul>

  <h2 style="margin-top:34px">Ask the patient’s - triage steps</h2>
  <ol class="steps">
    <li><b>1.</b> Confirm the patient’s name and phone number.</li>
    <li><b>2.</b> Does the patient attend the surgery? (ie Does the practice have previous medical records to hand?)</li>
    <li><b>3.</b> Location. <em>(“Are you at home?” “Are you alone?”)</em></li>
    <li><b>4.</b> Nature of their problem. (Patient may prefer to speak to the practice nurse or on call doctor.)</li>
    <li><b>5.</b> Duration of their symptoms. <em>(“How long have you felt like this?”)</em></li>
    <li><b>6.</b> Severity of their problem. <em>(“On a scale of 1 to 10 how severe is the pain?”</em> [if applicable].)</li>
    <li><b>7.</b> Any previous major health problems. <em>(“Are you on any medication?” “Do you have any allergies?”)</em></li>
  </ol>
</section>

<aside class="abs action-plan">
  <h3>EMERGENCY ACTION PLAN</h3>
  <ul>
    <li>• Remain calm and do not panic.</li>
    <li>• Be aware and respond to the needs of the emergency.</li>
    <li>• Assess which patient needs to take priority.</li>
    <li>• Deal with any injury or illness in order of severity.</li>
  </ul>
  <p class="call">CALL 000 FOR AMBULANCE, POLICE OR FIRE</p>
</aside>

<section class="abs panel panel-clinic">
  <h2>On the day emergencies in the clinic</h2>
  <p class="cat"><span class="c1">CATEGORY 1:</span> Patients should immediately be seen by the on-call doctor or other medical professional on duty.</p>
  <p class="cat"><span class="c2">CATEGORY 2:</span> Patients should be directed to the emergency department of their nearest hospital.</p>
  <p class="cat"><span class="c3">CATEGORY 3:</span> Patients or patients with worsening symptoms should be referred to the practice nurse or on call doctor.</p>
  <p class="cat"><span class="c4">CATEGORY 4:</span> Patients should be advised to attend the clinic immediately and triaged by the practice nurse (may then be slotted in between appointments or at the end of the session).</p>
  <p class="cat"><span class="c5">CATEGORY 5:</span> Patients should make an appointment for the day and be advised to call back if symptoms worsen.</p>
  <p class="cat"><span class="c6">CATEGORY 6:</span> Patients should make an appointment within 24 hours and call back if symptoms worsen.</p>
</section>

<section class="abs panel panel-disease">
  <h2><span class="justified">Patients presenting with symptoms of</span>potential communicable diseases</h2>
  <ul class="dots">
    <li>Such as ‘influenza’(‘flu), measles, chicken pox should be isolated to a secluded area of the medical practice such as the nurses’ office. Where possible, a notice of isolation is to be fixed to the door to limit access in this area.</li>
    <li>Patients with ‘flu like symptoms should be required to wear a surgical mask.</li>
    <li>If the patient is bleeding or vomiting, put gloves on before you assist them.</li>
  </ul>
</section>

<section class="abs panel panel-schedule">
  <h2>Scheduling care</h2>
  <ul class="dots">
    <li>Reception staff should reserve several unbooked appointment times each day for ‘on the day’ urgent appointments such as unwell children and the elderly, lacerations and suspected fractures.</li>
    <li>If your practice does not operate on an appointment system, patients should be triaged on walk in and advised of the expected waiting time to see the doctor, nurse or Aboriginal health worker.</li>
    <li>Where a patient is assessed as in need of urgent medical attention over the telephone, advise the caller to hang up and call 000 immediately for an ambulance.</li>
    <li>Where a receptionist is unable to determine the urgency of a telephone call, the patient should be transferred to the practice nurse or on-call doctor for triage.</li>
    <li>If a patient presents in person and requires urgent medical assistance after the doctor has left – call 000 for ambulance.</li>
    <li>Clinical staff treating the patient should wear as a minimum, a surgical mask, gloves and when collecting nose and/or throat swabs, protective eyewear.</li>
  </ul>
</section>

<p class="abs record-note">All emergency cases dealt with by reception should be recorded by the staff member involved in the patient health record in addition to the clinical notes recorded by the practice nurse or doctor/s treating the patient.</p>

<footer class="abs footer">
  <div>Whilst all care has been taken in preparing this document,<br>this information is a guide only and subject to change without notice.</div>
  <div class="credits">Harcourt College produced with permissions from Outback Care Alliance, produced by Outback Care Alliance with Clinic Circle Uptown with permissions from Southern Lakes Carewell Hub. Harcourt acknowledges the NBFPS Standards Criterion 3.2.3 Practice Training and Education in Triage.</div>
</footer>

</body>
</html>
```